Residential Remodeling Contractor needs updated business card

I need a new design for my business card.
Name of the company is Brookfell Construction. I need a card that commands presence, strength, integrity. I have been in business for 28 years. I am a Residential Remodeling Contractor that covers all aspects of a residential remodel and build.

```html
<!DOCTYPE html>
<html lang="en">
<head>
<meta charset="utf-8">
<title>Brookfell Construction – Business Card</title>
<link rel="stylesheet" href="https://fonts.googleapis.com/css2?family=Cinzel:wght@500&family=Poppins:wght@400;600&display=swap">
<style>
  :root{
    --backdrop:#1c1c1e;
    --card-blue:#213f80;
    --ink-white:#ffffff;
    --rule-blue:#5f79b6;
    --placeholder-tone:#3a5894;
  }
  *{margin:0;padding:0;box-sizing:border-box}
  html,body{width:1200px;height:1015px;overflow:hidden;background:var(--backdrop)}
  .canvas{position:relative;width:1200px;height:1015px}
  .card{
    position:absolute;left:250px;width:700px;height:400px;
    background:var(--card-blue);color:var(--ink-white);overflow:hidden;
    box-shadow:0 14px 30px rgba(0,0,0,.55);
  }
  .card--front{top:60px}
  .card--back{top:555px}

  /* Front */
  .brand{position:absolute;left:0;right:0;top:92px;text-align:center}
  .brand__name{
    font-family:"Cinzel",serif;font-weight:500;font-size:58px;line-height:1.02;
    letter-spacing:3px;color:var(--ink-white);
  }
  .brand__name span{display:block}
  .brand__name span + span{font-size:46px;letter-spacing:4px}
  .since{
    position:absolute;left:70px;right:70px;top:268px;display:flex;align-items:center;gap:16px;
    font-family:"Poppins",sans-serif;font-size:17px;
  }
  .since::before,.since::after{content:"";flex:1;height:1px;background:var(--rule-blue)}
  .tagline{
    position:absolute;left:0;right:0;top:312px;text-align:center;
    font-family:"Poppins",sans-serif;font-size:15px;letter-spacing:1.2px;text-transform:uppercase;
  }
  .tagline::after{
    content:"";display:block;margin:12px auto 0;width:560px;height:1px;background:var(--rule-blue);
  }

  /* Back */
  .illustration-area{
    position:absolute;left:30px;top:40px;width:200px;height:360px;
    background:linear-gradient(180deg,var(--placeholder-tone),#2c4a88);
  }
  .contact{position:absolute;left:300px;top:120px;font-family:"Poppins",sans-serif}
  .contact__name{font-weight:600;font-size:25px;letter-spacing:.5px;line-height:1.1}
  .contact__role{font-size:16px;margin-top:2px}
  .contact__address{font-size:15px;line-height:1.4;margin-top:26px}
  .contact__list{list-style:none;margin-top:22px;font-size:15px;line-height:1.6}
  .contact__list li{display:flex;align-items:center;gap:9px}
  .contact__list svg{width:16px;height:16px;flex:none}
</style>
</head>
<body>
<main class="canvas">

  <section class="card card--front" aria-label="Card front">
    <div class="brand">
      <h1 class="brand__name"><span>Brookfell</span><span>Construction</span></h1>
    </div>
    <p class="since">Since 28 years</p>
    <p class="tagline">Residential contractor for remodeling and build</p>
  </section>

  <section class="card card--back" aria-label="Card back">
    <div class="illustration-area" role="img" aria-label="Brand illustration area"></div>

    <div class="contact">
      <h2 class="contact__name">DANIEL HARTWELL</h2>
      <p class="contact__role">Managing Director</p>
      <p class="contact__address">421 Alder Ridge Road<br>Fairhaven, 45452</p>
      <ul class="contact__list">
        <li>
          <svg viewBox="0 0 24 24" fill="none" stroke="#fff" stroke-width="2.2" stroke-linecap="round" stroke-linejoin="round"><path d="M22 16.9v3a2 2 0 0 1-2.2 2A19.8 19.8 0 0 1 2.1 4.2 2 2 0 0 1 4.1 2h3a2 2 0 0 1 2 1.7c.1.9.4 1.8.7 2.7a2 2 0 0 1-.5 2.1L8 9.8a16 16 0 0 0 6 6l1.3-1.3a2 2 0 0 1 2.1-.4c.9.3 1.8.6 2.7.7a2 2 0 0 1 1.7 2z"/></svg>
          044-555 218 730
        </li>
        <li>
          <svg viewBox="0 0 24 24" fill="none" stroke="#fff" stroke-width="2.2" stroke-linejoin="round"><rect x="2" y="5" width="20" height="14"/><path d="M2 5l10 8 10-8"/></svg>
          info@brookfellbuild.com
        </li>
        <li>
          <svg viewBox="0 0 24 24" fill="none" stroke="#fff" stroke-width="2"><circle cx="12" cy="12" r="10"/><path d="M2 12h20M12 2c3 3 3 17 0 20M12 2c-3 3-3 17 0 20"/></svg>
          www.brookfellbuild.com
        </li>
      </ul>
    </div>
  </section>

</main>
</body>
</html>
```